Dalton Perriwether breaking. Or D. Perriwether breaking

I break in and train horses, any age any bread of horse, for any disaplin. I need a business card that is simple but effective, in the way of looking professional. I would like a horse on my card, preferably a horse without a rider. I also pre train horse, younge horses that need a bit of riding before they go into serious work, and prepare yearlings for sale.

Reason: This is for my boyfriend, and I really want it to be perfect and impressive!

Target Market(s)

Thoroughbred race horse trainers, horse industrie people.

Industry/Entity Type

Business

Contact Information for Business Card

Dalton Perriwether horse breaking, "WOLLOMBEE" Armidale, give your horse the right start to any career. dperri@mailzone.com.au, 0481392067. Horse breaking~pre-training~sale preparation

```html
<!DOCTYPE html>
<html lang="en">
<head>
<meta charset="utf-8">
<title>Dalton Perriwether Horse Breaking – Business Card</title>
<link rel="stylesheet" href="https://fonts.googleapis.com/css2?family=Jost:wght@400;600&display=swap">
<style>
  :root {
    --page: #ece9e4;
    --card-back: #e9ecef;
    --ink: #1c1c1e;
    --ink-soft: #2b2b2e;
    --band: #1a1714;
    --band-text: #d9c6a0;
    --sky-top: #6f7a86;
    --sky-mid: #a7a9a6;
    --sunset: #e0a23a;
    --sunset-deep: #c27418;
    --ground: #120f0c;
    --haze: rgba(120, 126, 136, 0.32);
    --haze-warm: rgba(224, 170, 90, 0.32);
    --shadow: rgba(0, 0, 0, 0.18);
  }
  * { box-sizing: border-box; margin: 0; padding: 0; }
  html, body { width: 1200px; height: 880px; overflow: hidden; }
  body {
    background: var(--page);
    font-family: "Jost", "Futura", sans-serif;
    position: relative;
  }
  .card {
    position: absolute;
    top: 275px;
    width: 540px;
    height: 330px;
    overflow: hidden;
    box-shadow: 0 6px 18px var(--shadow);
  }

  /* Front */
  .card--front { left: 40px; background: var(--band); }
  .front-photo {
    position: absolute;
    inset: 0 0 60px 0;
    background:
      radial-gradient(ellipse 45% 40% at 62% 88%, var(--sunset) 0%, var(--sunset-deep) 45%, transparent 80%),
      linear-gradient(180deg, var(--sky-top) 0%, var(--sky-mid) 40%, #b79560 68%, var(--ground) 86%, var(--ground) 100%);
  }
  .services {
    position: absolute;
    left: 0; right: 0; bottom: 0;
    height: 60px;
    padding: 0 20px;
    display: flex;
    align-items: center;
    justify-content: center;
    gap: 10px;
    color: var(--band-text);
    font-size: 17px;
    letter-spacing: 0.04em;
    text-transform: uppercase;
    white-space: nowrap;
  }
  .services .dot { font-size: 11px; }

  /* Back */
  .card--back { left: 620px; background: var(--card-back); }
  .back-photo {
    position: absolute;
    inset: 0;
    background:
      radial-gradient(ellipse 35% 40% at 45% 62%, var(--haze-warm) 0%, transparent 75%),
      radial-gradient(ellipse 60% 55% at 55% 60%, var(--haze) 0%, transparent 80%);
  }
  .tagline {
    position: absolute;
    top: 26px; left: 0; right: 0;
    text-align: center;
    font-size: 17px;
    letter-spacing: 0.04em;
    color: var(--ink-soft);
    text-transform: uppercase;
  }
  .name {
    position: absolute;
    top: 112px; left: 86px;
    font-weight: 600;
    font-size: 23px;
    letter-spacing: 0.2em;
    color: var(--ink);
    text-transform: uppercase;
  }
  .trade {
    position: absolute;
    top: 150px; left: 196px;
    font-size: 17px;
    letter-spacing: 0.05em;
    color: var(--ink-soft);
    text-transform: uppercase;
  }
  .contact {
    position: absolute;
    top: 214px; left: 60px;
    display: flex;
    gap: 16px;
    align-items: center;
    font-size: 17px;
    letter-spacing: 0.04em;
    color: var(--ink-soft);
  }
  .contact .phone { font-size: 20px; letter-spacing: 0.08em; }
  .contact .dot { font-size: 11px; }
</style>
</head>
<body>
  <section class="card card--front">
    <div class="front-photo" role="img" aria-label="Silhouettes of a herd of horses galloping across a ridge at sunset under a cloudy sky"></div>
    <p class="services">
      <span>Horse Breaking</span><span class="dot">●</span>
      <span>Pre-Training</span><span class="dot">●</span>
      <span>Sale Preparation</span>
    </p>
  </section>

  <section class="card card--back">
    <div class="back-photo" role="img" aria-label="Faded photo of horses galloping at sunset"></div>
    <p class="tagline">Give your horse the right start to any career.</p>
    <h1 class="name">Dalton Perriwether</h1>
    <p class="trade">Horse Breaking</p>
    <p class="contact">
      <span class="email">dperri@mailzone.com.au</span>
      <span class="dot">●</span>
      <span class="phone">0481 392 067</span>
    </p>
  </section>
</body>
</html>
```